High-end construction company needs a business card design

We need a modern looking business card that draws people in, is memorable and looks so good people will want to sick it on their fridges.
On the first side what is needed are:
Logo
My name - Tomas Verbelk
Title - Managing Director
Website - www.kravel.co.uk
Email - tomas@kravel.co.uk
Telephone - 020 5194 6381
Mobile - 07845319027
On the back side was is needed is a list of all the services we provide:
-Kitchen Renovations
-Bathroom Renovations
-House Renovations
-Garage Conversions
-Extensions
-Loft Conversions
-Conservatories
-Carpentry
-Tiling
-Electrical
-Plumbing & Heating
-Bricklaying
-Landscaping
-Decorating
-Plastering
We would like the colours to be the same shades as on the logo with grey or black for the words.
Target Market(s)
Anyone who needs building work done
Contact Information for Business Card
This business card is for a construction company which strives to deliver excellent service and quality.
The look and feel of the card should represent this.
Requirements
Must have
- On the first side what is needed are:
Logo
My name - Tomas Verbelk
Title - Managing Director
Website - www.kravel.co.uk
Email - tomas@kravel.co.uk
Telephone - 020 5194 6381
Mobile - 07845319027
Nice to have
- Cool looking features

```html
<!DOCTYPE html>
<html lang="en">
<head>
<meta charset="utf-8">
<title>Kravel Business Card</title>
<link rel="stylesheet" href="https://fonts.googleapis.com/css2?family=Montserrat:wght@400;500;700&display=swap">
<style>
  :root {
    --page: #f2f2f2;
    --charcoal: #383a39;
    --brand-green: #6cbf45;
    --name-green: #3a8f2a;
    --forest: #1a3d10;
    --paper: #f7f7f7;
    --ink-grey: #555a57;
    --white: #ffffff;
  }
  * { margin: 0; padding: 0; box-sizing: border-box; }
  html, body {
    width: 1200px; height: 1200px; overflow: hidden;
    background: var(--page);
    font-family: "Montserrat", sans-serif;
  }
  .card { position: absolute; left: 208px; width: 768px; height: 447px; }

  .card-front { top: 109px; background: var(--charcoal); }
  .front-wordmark {
    position: absolute; left: 0; right: 0; top: 300px;
    text-align: center; font-weight: 700; font-size: 96px;
    letter-spacing: 2px; color: var(--brand-green); line-height: 1;
  }
  .front-url {
    position: absolute; left: 0; right: 0; top: 416px;
    text-align: center; font-size: 10px; letter-spacing: 15px;
    color: var(--brand-green);
  }

  .card-back { top: 620px; height: 446px; background: var(--paper); }
  .contact-block { position: absolute; left: 51px; top: 36px; }
  .person-name { font-weight: 700; font-size: 20px; letter-spacing: 0.5px; color: var(--name-green); }
  .person-title { font-size: 11px; color: var(--ink-grey); margin-top: 4px; }
  .contact-list { list-style: none; margin-top: 26px; }
  .contact-list li { color: var(--ink-grey); font-size: 12px; height: 23px; display: flex; align-items: center; }
  .contact-list li.phone { font-size: 15px; letter-spacing: 0.5px; }
  .contact-label { font-weight: 700; font-size: 10px; color: var(--name-green); width: 26px; }

  .back-wordmark {
    position: absolute; left: 560px; top: 92px; width: 160px;
    text-align: center; font-weight: 700; font-size: 38px;
    color: var(--brand-green); line-height: 1;
  }

  .services-band {
    position: absolute; left: 0; right: 0; bottom: 0; height: 223px;
    background: var(--forest);
  }
  .services-heading {
    position: absolute; left: 52px; top: 12px;
    font-weight: 700; font-size: 13px; letter-spacing: 2px;
    color: var(--brand-green);
  }
  .services-column { position: absolute; top: 54px; list-style: none; }
  .services-column li {
    color: var(--white); font-size: 15px; letter-spacing: 2px;
    height: 27.5px; line-height: 27.5px;
  }
  .col-1 { left: 52px; } .col-2 { left: 299px; } .col-3 { left: 548px; }
</style>
</head>
<body>
  <section class="card card-front">
    <div class="front-wordmark">KRAVEL</div>
    <div class="front-url">www.kravel.co.uk</div>
  </section>

  <section class="card card-back">
    <div class="contact-block">
      <h1 class="person-name">TOMAS VERBELK</h1>
      <p class="person-title">Managing Director</p>
      <ul class="contact-list">
        <li class="phone"><span class="contact-label">T :</span>020 5194 6381 , 07845319027</li>
        <li><span class="contact-label">E :</span>tomas@kravel.co.uk</li>
        <li><span class="contact-label">W :</span>www.kravel.co.uk</li>
      </ul>
    </div>
    <div class="back-wordmark">KRAVEL</div>

    <div class="services-band">
      <h2 class="services-heading">Our Services</h2>
      <ul class="services-column col-1">
        <li>-Carpentry</li><li>-Tiling</li><li>-Electrical</li><li>-Plumbing &amp; Heating</li><li>-House Renovations</li>
      </ul>
      <ul class="services-column col-2">
        <li>-Landscaping</li><li>-Decorating</li><li>-Bathroom Renovations</li><li>-Kitchen Renovations</li><li>-Plastering</li>
      </ul>
      <ul class="services-column col-3">
        <li>-Conservatories</li><li>-Bricklaying</li><li>-Garage Conversions</li><li>-Extensions</li><li>-Loft Conversions</li>
      </ul>
    </div>
  </section>
</body>
</html>
```